New Business Card for Web Design/Internet Marketing Company

Looking for a great looking new business card. We are a 10 year old web design, internet marketing and website management company that works mostly with small businesses.

Our new card needs to better match the colors and style of our website, be bold, extremely usable and slightly edgy.

Target Market(s)

Small/Medium businesses that have websites

Industry/Entity Type

Internet

Requirements
Must have
• Front and back design, full color, rounded corners please

Must use the colors/style of our website (JPG provided)

INFO FOR CARDS (as readable as possible please)
Mark Pellow
President/CEO
mark@brightlanesites.com
Phone: 520-481-7093
Toll Free: 866-481-7093
Address: 4315 E. Kestrel Ave. Ste. 140, Tucson, AZ 85733

THINGS I WANT TO PROMOTE (if there is room):
1. Our Website - www.brightlanesites.com

2. Social Media
Twitter: @brightlanesites
Facebook: www.facebook.com/brightlanesites

3. Our Services
Web Design
Internet Marketing
Website Management

```html
<!DOCTYPE html>
<html lang="en">
<head>
<meta charset="utf-8">
<title>Brightlane Sites – Business Card</title>
<link href="https://fonts.googleapis.com/css2?family=Source+Sans+3:wght@400;600;700&display=swap" rel="stylesheet">
<style>
  :root {
    --stage: #e9e6e2;
    --card-white: #ffffff;
    --card-grey: #5f5f61;
    --card-grey-dark: #58585a;
    --brand-blue: #1b8fc6;
    --brand-orange: #f07f27;
    --ink: #444446;
    --ink-soft: #555557;
    --on-dark: #ffffff;
  }
  * { margin: 0; padding: 0; box-sizing: border-box; }
  html, body { width: 1200px; height: 402px; overflow: hidden; }
  body {
    background: var(--stage);
    font-family: "Source Sans 3", "Helvetica Neue", Arial, sans-serif;
    position: relative;
  }
  .card {
    position: absolute;
    top: 56px;
    width: 512px;
    height: 292px;
    border-radius: 26px;
    overflow: hidden;
    box-shadow: 0 3px 10px rgba(0,0,0,0.25);
  }
  .card--front { left: 64px; background: var(--card-white); }
  .card--back { left: 629px; background: var(--card-grey); color: var(--on-dark); }

  .front-wave { position: absolute; inset: 0; width: 100%; height: 100%; }

  .brand-name {
    position: absolute;
    left: 36px; top: 100px;
    font-size: 34px; font-weight: 700;
    color: var(--brand-blue);
    letter-spacing: -0.5px;
    line-height: 1;
  }
  .person { position: absolute; right: 28px; top: 34px; text-align: right; }
  .person__name { font-size: 19px; font-weight: 700; color: var(--brand-blue); line-height: 1.1; }
  .person__title { font-size: 13.5px; color: var(--ink); line-height: 1.2; }

  .address {
    position: absolute; left: 36px; top: 198px;
    font-size: 13.5px; line-height: 1.05; color: var(--ink-soft);
  }
  .contact-list {
    position: absolute; right: 26px; top: 206px;
    list-style: none; text-align: right;
    font-size: 13.5px; line-height: 19.5px; color: var(--on-dark);
  }
  .contact-list li { display: flex; justify-content: flex-end; align-items: center; gap: 8px; }
  .contact-list svg { width: 10px; height: 10px; flex: none; }

  .back-brand {
    position: absolute; left: 34px; top: 118px;
    display: flex; align-items: center; gap: 12px;
    font-size: 38px; font-weight: 700; color: var(--on-dark);
    line-height: 1;
  }
  .back-brand__dot { width: 22px; height: 22px; border-radius: 50%; background: var(--on-dark); }

  .social { position: absolute; left: 270px; top: 40px; list-style: none; font-size: 17px; line-height: 25px; }
  .social li { display: flex; align-items: center; gap: 9px; }
  .social__mark { width: 15px; height: 15px; border-radius: 3px; background: var(--brand-blue); }

  .services { position: absolute; left: 270px; top: 114px; }
  .services__title { font-size: 25px; font-weight: 600; margin-bottom: 18px; line-height: 1; }
  .services__list { list-style: none; font-size: 22px; line-height: 31px; }
</style>
</head>
<body>
  <section class="card card--front">
    <svg class="front-wave" viewBox="0 0 512 292" preserveAspectRatio="none" aria-hidden="true">
      <path d="M0 246 C70 262 140 258 230 232 C320 204 420 166 512 166 L512 292 L0 292 Z" fill="var(--card-grey)"/>
      <path d="M0 238 C70 256 140 252 230 226 C320 198 420 158 512 156" fill="none" stroke="var(--brand-blue)" stroke-width="4"/>
      <path d="M0 244 C70 260 140 256 230 230 C320 202 420 164 512 163" fill="none" stroke="var(--card-white)" stroke-width="3"/>
    </svg>

    <div class="brand-name">Brightlane Sites</div>

    <div class="person">
      <div class="person__name">Mark Pellow</div>
      <div class="person__title">President/CEO</div>
    </div>

    <address class="address" style="font-style:normal">
      4315 E. Kestrel Ave., Ste. 140<br>Tucson, AZ 85733
    </address>

    <ul class="contact-list">
      <li>520-481-7093 <svg viewBox="0 0 10 10"><circle cx="5" cy="5" r="4.3" fill="none" stroke="#fff" stroke-width="1.2"/><path d="M3 3 L7 7" stroke="#fff" stroke-width="1.4"/></svg></li>
      <li>866-481-7093 <svg viewBox="0 0 10 10"><circle cx="5" cy="5" r="4.3" fill="none" stroke="#fff" stroke-width="1.2"/><path d="M7 3 L3 7" stroke="#fff" stroke-width="1.4"/></svg></li>
      <li>mark@brightlanesites.com <svg viewBox="0 0 10 10"><rect x="0.5" y="2" width="9" height="6" fill="#fff"/><path d="M0.5 2 L5 5.5 L9.5 2" fill="none" stroke="var(--card-grey)" stroke-width="1"/></svg></li>
      <li>www.brightlanesites.com <svg viewBox="0 0 10 10"><circle cx="5" cy="5" r="4.3" fill="none" stroke="#fff" stroke-width="1.2"/><path d="M0.7 5 H9.3 M5 0.7 V9.3" stroke="#fff" stroke-width="1"/></svg></li>
    </ul>
  </section>

  <section class="card card--back">
    <div class="back-brand"><span class="back-brand__dot"></span>Brightlane</div>

    <ul class="social">
      <li><span class="social__mark"></span>@brightlanesites</li>
      <li><span class="social__mark"></span>brightlanesites</li>
    </ul>

    <div class="services">
      <h2 class="services__title">Our Services</h2>
      <ul class="services__list">
        <li>Web Design</li>
        <li>Internet Marketing</li>
        <li>Website Management</li>
      </ul>
    </div>
  </section>
</body>
</html>
```